Lotus Harvest Catering Group - Business Card Design

We are premium Asian Catering Company based in Melbourne. We specialize in full service sit down banquets.

Industry/Entity Type

Business

Contact Information for Business Card

Lotus Harvest Catering Group
17b Carrowbrook Ave Tillford 3158
P: 03 9417 2685 | M: 0438 627 951
www.lotusharvestcatering.com.au
info@lotusharvestcatering.com.au

```html
<!DOCTYPE html>
<html lang="en">
<head>
<meta charset="utf-8">
<title>Lotus Harvest Catering Group – Business Card</title>
<link rel="stylesheet" href="https://fonts.googleapis.com/css2?family=Jost:wght@400;500&display=swap">
<style>
  :root {
    --backdrop: #d9d9d9;
    --card-black: #0b0b0b;
    --pattern-dark: #1c1c1c;
    --pattern-mid: #262626;
    --accent-red: #d3141c;
    --label-red: #e02a2f;
    --text-white: #f2f2f2;
    --text-grey: #9a9a9a;
    --logo-silver: #d6d6d6;
  }
  * { margin: 0; padding: 0; box-sizing: border-box; }
  html, body { width: 1200px; height: 900px; overflow: hidden; }
  body {
    background: var(--backdrop);
    font-family: "Jost", "Futura", sans-serif;
    display: flex;
    align-items: center;
    justify-content: center;
    gap: 30px;
  }
  .card {
    position: relative;
    width: 560px;
    height: 342px;
    background: var(--card-black);
    overflow: hidden;
  }
  .damask-field {
    position: absolute;
    inset: 0;
    background: radial-gradient(ellipse at 50% 40%, var(--pattern-mid) 0%, var(--pattern-dark) 55%, var(--card-black) 100%);
  }
  .card-back .damask-field {
    bottom: auto;
    height: 150px;
  }
  .brand {
    position: absolute;
    display: flex;
    align-items: center;
    gap: 12px;
    color: var(--logo-silver);
    font-weight: 500;
    letter-spacing: 0.06em;
    text-transform: uppercase;
    white-space: nowrap;
  }
  .brand-dot {
    width: 14px; height: 14px;
    border-radius: 50%;
    background: var(--accent-red);
    flex: none;
  }
  .card-front .brand {
    left: 50%; top: 50%;
    transform: translate(-50%, -50%);
    font-size: 22px;
  }
  .card-back .brand {
    left: 50%; top: 72px;
    transform: translateX(-40%);
    font-size: 17px;
  }
  .brand-dot-small { width: 11px; height: 11px; }
  .red-rule {
    position: absolute;
    left: 0; right: 0;
    top: 150px;
    height: 5px;
    background: var(--accent-red);
  }
  .contact-list {
    position: absolute;
    left: 30px; top: 178px;
    list-style: none;
    font-size: 14px;
    line-height: 1.45;
  }
  .contact-label { color: var(--label-red); margin-right: 6px; }
  .contact-value { color: var(--text-white); }
  .address {
    position: absolute;
    right: 34px; bottom: 24px;
    font-size: 14px;
    line-height: 1.35;
    color: var(--text-grey);
  }
  .address .contact-label { display: block; }
</style>
</head>
<body>

  <section class="card card-front" aria-label="Business card front">
    <div class="damask-field" role="img" aria-label="Dark tone-on-tone floral damask pattern"></div>
    <div class="brand"><span class="brand-dot"></span>Lotus Harvest Catering Group</div>
  </section>

  <section class="card card-back" aria-label="Business card back">
    <div class="damask-field" role="img" aria-label="Dark tone-on-tone floral damask pattern"></div>
    <div class="brand"><span class="brand-dot brand-dot-small"></span>Lotus Harvest Catering Group</div>
    <div class="red-rule"></div>
    <ul class="contact-list">
      <li><span class="contact-label">phone:</span><span class="contact-value">03 9417 2685</span></li>
      <li><span class="contact-label">mobile:</span><span class="contact-value">0438 627 951</span></li>
      <li><span class="contact-label">email:</span><span class="contact-value">info@lotusharvestcatering.com.au</span></li>
      <li><span class="contact-label">web:</span><span class="contact-value">www.lotusharvestcatering.com.au</span></li>
    </ul>
    <address class="address" style="font-style:normal">
      <span class="contact-label">Address:</span>
      17b Carrowbrook Ave.<br>
      Tillford 3158
    </address>
  </section>

</body>
</html>
```